Clear Meadow Beauty Product Labels for VERITAS certified skin care products

Design a label template for my certified organic skin care products. I need to be able to edit this label for each product.
Packaging will either be white or black (not yet decided) PET boston bottles ranging from 50mL to 500mL sizes (www.kelbrovessels.com.au), 15mL size Tosni PET bottle (www.marlowsupply.com.au)
Types of products include body wash (500mL), body lotion (500mL), facial cleansers (100mL), face and hand creams (50mL), and eye cream (15mL). More products will be developed such as body scrub, shampoo and conditioner.

Target Market(s)

30 - 55 year old women, middle to high income, living on the Northern Rivers NSW Australia

Industry/Entity Type

Cosmetics

Colors

Designer to choose colors to be used in the design.

Requirements
Must have
• Space on front (or middle if rectangular) of label for product name, volume/mass (note: I need to be able to adjust the size of the volume/mass to suit the packaging, also it needs to be at least 2mm from the limits of the package and separate by at least 2mm in all directions from other graphics), VERITAS ORGANIC logo with SVN bud (products will be certified by Southern Verified Natural (SVN) under the VERITAS standard - refer to SVN labelling attached for VERITAS SVN bud), space for marketing message, and my business logo.
• Space on back (or sides if rectangular) for name and address of company (Clear Meadow Beauty, 17 Brennock Road, Fernvale Rise NSW 2999), ingredients list, directions for use, claims of product ('x% organic of total', '100% natural ingredients', I need to be able to add claims for each product), storage, batch number and expiry date, space for safety instructions.
Nice to have
• Simple
• Space on front for picture of key ingredient
• Background a neutral colour
• Use of green and brown colours
Should not have
• Too crowded

```html
<!DOCTYPE html>
<html lang="en">
<head>
<meta charset="utf-8">
<title>Clear Meadow Beauty – Body Wash Label</title>
<link rel="stylesheet" href="https://fonts.googleapis.com/css2?family=Questrial&display=swap">
<style>
  :root {
    --leaf-green: #55963f;
    --maroon: #330810;
    --ink: #3a0a12;
    --paper: #ffffff;
  }
  * { margin: 0; padding: 0; box-sizing: border-box; }
  html, body { width: 1200px; height: 856px; overflow: hidden; background: var(--paper); }
  .label {
    position: relative; width: 1200px; height: 856px;
    font-family: "Questrial", sans-serif; color: var(--ink);
  }
  .brand-band {
    position: absolute; left: 0; top: 0; width: 100%; height: 160px;
    background: var(--leaf-green);
    display: flex; align-items: center; justify-content: center; gap: 14px;
  }
  .brand-dot { width: 40px; height: 40px; border: 2px solid var(--paper); border-radius: 50%; }
  .brand-name { color: var(--paper); font-size: 34px; letter-spacing: 1px; }
  .range-band {
    position: absolute; left: 0; top: 160px; width: 100%; height: 42px;
    background: var(--maroon); color: var(--paper);
    font-size: 19px; text-align: center; line-height: 42px; letter-spacing: 0.3px;
  }
  .column { position: absolute; top: 230px; width: 300px; }
  .column-left { left: 30px; }
  .column-right { left: 868px; }
  .section-title { font-size: 13.6px; font-weight: 700; margin-bottom: 17px; letter-spacing: 0.3px; }
  .section-text {
    font-size: 14.4px; line-height: 15.2px; text-align: justify; margin-bottom: 15px;
    hyphens: auto; -webkit-hyphens: auto; letter-spacing: -0.2px;
  }
  .section-text + .section-title { margin-top: 7px; }
  .product-title { position: absolute; left: 360px; width: 480px; text-align: center; }
  .product-line { top: 300px; font-size: 32px; }
  .product-type { top: 340px; font-size: 68px; letter-spacing: 1px; line-height: 80px; }
  .tagline { position: absolute; left: 400px; width: 400px; top: 472px; text-align: center; font-size: 16.5px; font-style: italic; line-height: 18px; }
  .cert-badge { position: absolute; left: 530px; top: 648px; width: 134px; height: 64px; border: 2px solid var(--leaf-green); border-radius: 4px; background: #eef5ea; }
  .standard-name { position: absolute; left: 500px; width: 200px; top: 720px; text-align: center; font-size: 30px; line-height: 28px; letter-spacing: 1px; }
  .fine-print { position: absolute; left: 870px; width: 106px; font-size: 11px; font-style: italic; line-height: 11.4px; }
  .claim { top: 500px; }
  .company-address { top: 578px; }
  .icon { position: absolute; left: 870px; }
  .volume-band {
    position: absolute; left: 0; top: 798px; width: 100%; height: 39px;
    background: var(--leaf-green); color: var(--paper);
    font-size: 27px; text-align: center; line-height: 39px;
  }
</style>
</head>
<body>
<main class="label">
  <header class="brand-band">
    <span class="brand-dot"></span>
    <span class="brand-name">Clear Meadow Beauty</span>
  </header>
  <div class="range-band">LOREM IPSUM DOLOR</div>

  <section class="column column-left" lang="en">
    <h2 class="section-title">DIRECTIONS FOR USE:</h2>
    <p class="section-text">Lorem ipsum dolor sit amet, consectetuer adipiscing elit, sed diam nonummy nibh euismod tincidunt ut laoreet dolore magna aliquam erat volutpat. Ut wisi enim ad minim veniam, quis nostrud exerci tation ullamcorper suscipit lobortis nisl ut aliquip ex ea commodo conse.</p>
    <p class="section-text">Lorem ipsum dolor sit amet, consectetuer adipiscing elit, sed diam nonummy nibh euis.</p>
    <h2 class="section-title">INGREDIENTS:</h2>
    <p class="section-text">Lorem ipsum dolor sit amet, consectetuer adipiscing elit, sed diam nonummy nibh euismod tincidunt ut laoreet dolore magna aliquam erat volutpat. Ut wisi enim ad minim veniam, quis nostrud exerci tation ullamcorper suscipit lobortis nisl ut aliquip ex ea commodo consequat. Duis autem vel eum iriure dolor in hendrerit in vulputate velit esse molestie consequat, vel illum dolore eu feugiat nulla facilisis at vero eros et accumsan et iusto odio dignissim qui blandit praesent luptatum zzril delenit augue duis dolore te feugait nulla facilisi. Lorem ipsum dolor sit amet, cons ectetuer adipiscing elit, sed diam nonummy nibh euismod tincidunt ut laoreet dolore magna aliquam erat volutpat. Ut wisi enim ad minim veniam, quis nostrud exerci tation ullamcorper suscipit lobortis nisl ut aliquip ex ea commodo consequat.</p>
  </section>

  <p class="product-title product-line">Lorem Ipsum Dolor</p>
  <h1 class="product-title product-type">BODY WASH</h1>
  <p class="tagline">Lorem ipsum dolor sit amet,<br>consectetuer adipiscin</p>

  <div class="cert-badge" role="img" aria-label="Certification badge"></div>
  <p class="standard-name">VERITAS<br>ORGANIC</p>

  <section class="column column-right" lang="en">
    <h2 class="section-title">MARKETING MESSAGE:</h2>
    <p class="section-text">Lorem ipsum dolor sit amet, consectetuer adipiscing elit, sed diam nonummy nibh euismod tincidunt ut laoreet dolore magna aliquam erat volutpat. Ut wisi enim ad minim veniam, quis nostrud exerci tation ullamcorper suscipit lobortis nisl ut aliquip ex ea commodo conse.</p>
    <p class="section-text">Lorem ipsum dolor sit amet, consectetuer adipiscing elit, sed diam nonummy nibh euismod tincidunt ut laoreet dolore magna aliquam erat volutpat. Ut wisi enim ad minim veniam, quis nostrud exerci tation ullamcorper suscipit lobortis nisl ut aliquip ex ea commodo</p>
  </section>

  <p class="fine-print claim">Lorem ipsum dolor sit amet, consectetuer adipiscing elit, diam nonummy nibh euismod tincidunt ut.</p>
  <p class="fine-print company-address">Clear Meadow Beauty,<br>17 Brennock Road,<br>Fernvale Rise<br>NSW 2999</p>

  <svg class="icon" style="top:646px" width="54" height="52" viewBox="0 0 54 52" role="img" aria-label="Recyclable">
    <g fill="none" stroke="#55963f" stroke-width="7" stroke-linejoin="round">
      <path d="M20 8 L27 4 L34 12"/>
      <path d="M44 24 L48 34 L40 44"/>
      <path d="M22 46 L10 46 L6 34"/>
    </g>
    <g fill="#55963f">
      <polygon points="38,4 40,18 28,14"/>
      <polygon points="30,40 42,36 38,50"/>
      <polygon points="2,26 14,30 4,40"/>
    </g>
  </svg>

  <svg class="icon" style="top:706px" width="56" height="62" viewBox="0 0 56 62" role="img" aria-label="Period after opening 6 months">
    <g fill="none" stroke="#55963f" stroke-width="2">
      <ellipse cx="22" cy="14" rx="18" ry="6" transform="rotate(-25 22 14)"/>
      <path d="M6 30 H52 V50 Q52 58 44 58 H14 Q6 58 6 50 Z"/>
    </g>
    <text x="29" y="52" text-anchor="middle" font-family="Questrial, sans-serif" font-size="17" fill="#55963f">6M</text>
  </svg>

  <footer class="volume-band">16 FL OZ/ 500ML</footer>
</main>
</body>
</html>
```